Health Coach needs a Business Card Design

Need a really modern feminine business card design for a health and lifestyle coach. Needs to use geometric shapes, muted grey/blue/green pastels and black and white - see mood board attached and logo. The client likes black and white, modern, san serif with the use of lines and possibly a shadow leaf as in the mood board. Possibly put the tag line on the back or an icon of the logo. Logo is also attached. An icon of the logo would be great too.

Target Market(s)

Women (some men) aged 30 to 50.

Industry/Entity Type

Business

Contact Information for Business Card

Maren Tolvey
e-mail: hello@marentwell.net
website: marentwell.net
Phone: +610497268153

The tag line is "A balanced body for Life"

Font styles to use
Sans Serif

Colors
ecf7fb
cfeae6
000000
ffffff
f5f5f5

Requirements
Must have
• Black and white, logo, tag line and details
Nice to have
• Would be nice to incorporate the shadow palm.fern leaves as in the mood board and or geometric lines/shapes - see mood board. Could be either standard rectangle or would be happy with square too.
Should not have
• Flowers or decorations

```html
<!DOCTYPE html>
<html lang="en">
<head>
<meta charset="utf-8">
<title>Maren T – Business Card</title>
<link href="https://fonts.googleapis.com/css2?family=Heebo:wght@300;400&display=swap" rel="stylesheet">
<style>
  :root {
    --stage: #1f1f1f;
    --card-back: #808080;
    --card-front: #ecf7fb;
    --ink: #000000;
    --ink-soft: #111111;
  }
  html, body {
    margin: 0;
    padding: 0;
    overflow: hidden;
  }
  .canvas {
    position: relative;
    width: 1200px;
    height: 741px;
    background: var(--stage);
    overflow: hidden;
    font-family: "Heebo", sans-serif;
    color: var(--ink);
  }
  .card {
    position: absolute;
    top: 229px;
    width: 494px;
    height: 282px;
    border-radius: 12px;
  }
  .card--back {
    left: 100px;
    background: var(--card-back);
  }
  .card--front {
    left: 606px;
    background: var(--card-front);
  }
  .brand {
    position: absolute;
    display: flex;
    flex-direction: column;
  }
  .brand__name {
    font-weight: 300;
    font-size: 36px;
    line-height: 1;
    letter-spacing: 0.08em;
  }
  .brand__tagline {
    margin-top: 10px;
    font-weight: 400;
    font-size: 10.5px;
    line-height: 11px;
    letter-spacing: 0.34em;
    text-transform: uppercase;
  }
  .card--back .brand {
    left: 0;
    right: 0;
    top: 114px;
    align-items: center;
  }
  .card--back .brand__tagline {
    margin-left: 0.34em;
  }
  .card--front .brand {
    right: 26px;
    top: 41px;
    align-items: flex-end;
  }
  .card--front .brand__tagline {
    margin-right: -0.34em;
  }
  .holder {
    position: absolute;
    left: 29px;
    top: 171px;
    margin: 0;
    font-weight: 400;
    font-size: 17.5px;
    line-height: 1;
    letter-spacing: 0.08em;
    text-transform: uppercase;
  }
  .contact {
    position: absolute;
    left: 29px;
    top: 208px;
    margin: 0;
    font-size: 14px;
    line-height: 16.5px;
    font-weight: 400;
    letter-spacing: 0.01em;
    color: var(--ink-soft);
  }
</style>
</head>
<body>
  <main class="canvas">
    <section class="card card--back" aria-label="Card back">
      <div class="brand">
        <span class="brand__name">Maren T</span>
        <span class="brand__tagline">A balanced body for life</span>
      </div>
    </section>

    <section class="card card--front" aria-label="Card front">
      <div class="brand">
        <span class="brand__name">Maren T</span>
        <span class="brand__tagline">A balanced body for life</span>
      </div>
      <h1 class="holder">Maren Tolvey</h1>
      <p class="contact">
        <span class="contact__label">e-mail:</span> hello@marentwell.net<br>
        <span class="contact__label">website:</span> marentwell.net<br>
        <span class="contact__label">Phone:</span> +610497268153
      </p>
    </section>
  </main>
</body>
</html>
```